Business Card Design

We have our logo and everything in place. Looking to have a layout for our new business cards designed. These will be printed with a matte finish, possibly rounded corners, and looking to incorporate some cool spot UV layers into the design.

Ive uploaded the existing card front and back as well as our logo.

Card Size Will Be 3.5" x 2"

Industry/Entity Type

Business

```html
<!DOCTYPE html>
<html lang="en">
<head>
<meta charset="utf-8">
<title>Ridgeline Deck and Rail – Business Cards</title>
<link rel="stylesheet" href="https://fonts.googleapis.com/css2?family=Crimson+Text:wght@400;600&display=swap">
<style>
  :root {
    --backdrop: #dcdde0;
    --card: #000000;
    --ink: #ffffff;
    --accent: #2a86cf;
  }
  * { box-sizing: border-box; margin: 0; padding: 0; }
  html, body {
    width: 894px;
    height: 1200px;
    overflow: hidden;
    background: var(--backdrop);
  }
  .sheet {
    width: 894px;
    height: 1200px;
    display: flex;
    justify-content: center;
    align-items: center;
    gap: 60px;
  }
  .card {
    width: 360px;
    height: 630px;
    background: var(--card);
    border-radius: 34px;
    color: var(--ink);
    font-family: "Crimson Text", Georgia, serif;
    display: flex;
    flex-direction: column;
    align-items: center;
  }
  .card--front { justify-content: center; }
  .card--back { padding-top: 92px; }

  .wordmark {
    text-align: center;
    font-family: "Crimson Text", Georgia, serif;
    font-weight: 400;
    color: var(--ink);
    line-height: 1;
  }
  .wordmark__name { display: block; font-size: 56px; }
  .wordmark__tag {
    display: block;
    font-size: 22px;
    letter-spacing: 2px;
    text-transform: uppercase;
    margin-top: 6px;
  }

  .contact-person {
    margin-top: 68px;
    text-align: center;
    text-transform: uppercase;
  }
  .contact-person__name { font-size: 22px; font-weight: 600; letter-spacing: 0.3px; }
  .contact-person__role { font-size: 17px; margin-top: 2px; }

  .contact-list {
    list-style: none;
    width: 312px;
    margin-top: 22px;
  }
  .contact-list__item { text-align: center; margin-top: 14px; }
  .contact-list__divider {
    display: flex;
    align-items: center;
    gap: 8px;
  }
  .contact-list__divider::before,
  .contact-list__divider::after {
    content: "";
    flex: 1;
    height: 2px;
    background: var(--accent);
  }
  .contact-list__icon { width: 18px; height: 18px; display: block; }
  .contact-list__text { font-size: 18px; margin-top: 6px; display: block; letter-spacing: 0.2px; }
</style>
</head>
<body>
<main class="sheet">
  <section class="card card--front" aria-label="Card front">
    <div class="wordmark">
      <span class="wordmark__name">Ridgeline</span>
      <span class="wordmark__tag">Deck and Rail</span>
    </div>
  </section>

  <section class="card card--back" aria-label="Card back">
    <div class="wordmark">
      <span class="wordmark__name">Ridgeline</span>
      <span class="wordmark__tag">Deck and Rail</span>
    </div>

    <div class="contact-person">
      <p class="contact-person__name">Daniel Carver</p>
      <p class="contact-person__role">President</p>
    </div>

    <ul class="contact-list">
      <li class="contact-list__item">
        <div class="contact-list__divider">
          <svg class="contact-list__icon" viewBox="0 0 24 24" aria-hidden="true">
            <path fill="#2a86cf" d="M6.6 10.8a15.1 15.1 0 0 0 6.6 6.6l2.2-2.2c.3-.3.7-.4 1-.2 1.1.4 2.3.6 3.6.6.6 0 1 .4 1 1V20c0 .6-.4 1-1 1A17 17 0 0 1 3 4c0-.6.4-1 1-1h3.5c.6 0 1 .4 1 1 0 1.3.2 2.5.6 3.6.1.3 0 .7-.2 1z"/>
          </svg>
        </div>
        <span class="contact-list__text">555.010.7381</span>
      </li>
      <li class="contact-list__item">
        <div class="contact-list__divider">
          <svg class="contact-list__icon" viewBox="0 0 24 24" aria-hidden="true">
            <rect x="2" y="5" width="20" height="14" fill="#2a86cf"/>
            <path d="M2 5l10 8 10-8" fill="none" stroke="#000" stroke-width="1.6"/>
          </svg>
        </div>
        <span class="contact-list__text">ridgelinedeckandrail@mail.com</span>
      </li>
      <li class="contact-list__item">
        <div class="contact-list__divider">
          <svg class="contact-list__icon" viewBox="0 0 24 24" aria-hidden="true">
            <circle cx="12" cy="12" r="10" fill="#2a86cf"/>
            <g fill="none" stroke="#000" stroke-width="1.2">
              <ellipse cx="12" cy="12" rx="4.5" ry="10"/>
              <line x1="2" y1="12" x2="22" y2="12"/>
              <line x1="12" y1="2" x2="12" y2="22"/>
              <path d="M4 7h16M4 17h16"/>
            </g>
          </svg>
        </div>
        <span class="contact-list__text">www.ridgelinedeckandrail.com</span>
      </li>
    </ul>
  </section>
</main>
</body>
</html>
```